levyreadynow.com website design (promote tax and financial services)

I need web design layouts for a 4-6 page website for a finance and tax services business.

Assumptions:
-Responsive design for desktop, laptop, tablet and mobile
-website will not be programmed with any flash elements
-Animation is welcomed
-stock photography may be required (royalty free preferred)
-Prefer to stay away from designs with large images that result in long loading times
-Web design will be pulled through to other digital and print promotional materials that the company develops

The audience is primarily male. Attached is the site and content map, including the company logo

Target Market(s)

individuals and small-to-medium business owners
Primary geographic market = NYC metropolitan area
Secondary geographic market = East Coast USA
Tertiary geographic market = National USA

Any stock photography should represent a diverse population

Industry/Entity Type

Financial Service

Number of Pages Required

5+ page

Font styles to use
Sans Serif

Colors
0758a4
9bcb3b

Requirements
Must have
• -Responsive design that translates nicely to mobile and tablet devices
• -Simple, clean but yet sophisticated design
• -Be in alignment with or a derivative of the logo design (provided with PPT attachment)
• -Compatibility with website programming and coding software
• -Include a countdown to the tax deadline (April 18, 2016)
• -Web-friendly fonts
• -Search box
• -Link to social media properties (via social icons)
• -Include company phone number and clickable link to activate ability to contact company by email
Nice to have
• -Simple animation, as long as it does not impact load time
• -Engaging call-to-action buttons
• -Rotating homepage banners
• -Original icons
• -"About Us" page should have a friendlier, welcoming design
• -Image/Photo caption examples
• -Assume that copy (text) can be minimized to accommodate more visual displays
• -"Continue reading" or "read more" links to expand truncated copy are welcomed
• -A pricing table (not a priority, but nice to have)
Should not have
• Overcrowded design (don't be afraid of white space, if needed)
• too many bells and whistles (flash animation, moving cursors etc.)

```html
<!DOCTYPE html>
<html lang="en">
<head>
<meta charset="utf-8">
<title>levyreadynow.com</title>
<link href="https://fonts.googleapis.com/css2?family=Noto+Serif:wght@400;700&display=swap" rel="stylesheet">
<style>
:root{
  --blue:#0758a4;
  --blue-dark:#0a4a8c;
  --blue-mid:#3a7cc4;
  --green:#9bcb3b;
  --green-dark:#7db42a;
  --text:#555;
  --white:#fff;
}
*{margin:0;padding:0;box-sizing:border-box}
html,body{width:734px;height:1200px;overflow:hidden}
body{font-family:"Noto Serif",Georgia,serif;background:var(--white);position:relative;color:var(--text)}
.abs{position:absolute}
/* header */
.site-header{left:0;top:0;width:734px;height:66px;background:linear-gradient(#0a5aa6,#074a8e);border-bottom:3px solid var(--green)}
.top-info{top:11px;font-size:6.5px;color:var(--white);display:flex;align-items:center;gap:4px}
.btn-appointment{left:408px;top:8px;width:104px;height:17px;background:linear-gradient(#a9d64a,var(--green-dark));color:var(--white);font-size:6px;display:flex;align-items:center;justify-content:center;border-radius:2px}
.search{left:520px;top:8px;width:126px;height:17px;background:#0a3f78;border:1px solid #2d6cb0;color:var(--white);font-size:6.5px;padding:0 6px;display:flex;align-items:center;justify-content:space-between;border-radius:2px}
.logo{left:87px;top:30px;width:67px;height:31px;background:var(--white);display:flex;align-items:center;justify-content:center;flex-direction:column;color:var(--blue);font-size:12px;font-weight:700;line-height:1}
.logo small{font-size:5.5px;font-weight:400;margin-top:3px}
.main-nav a{position:absolute;top:39px;font-size:8px;color:var(--white);text-decoration:none;transform:translateX(-50%);white-space:nowrap}
.main-nav a.active{color:var(--green)}
.nav-marker{left:269px;top:59px;width:0;height:0;border-left:5px solid transparent;border-right:5px solid transparent;border-bottom:4px solid var(--green)}
/* hero */
.hero-photo{left:0;top:66px;width:734px;height:276px;background:linear-gradient(100deg,#d9cfc2 0%,#eadfd1 35%,#e3b79a 65%,#c99272 100%)}
.hero-panel{left:88px;top:142px;width:269px;height:168px;background:rgba(255,255,255,.86);border-radius:3px;padding:12px 10px}
.hero-panel h2{font-size:11px;font-weight:400;color:var(--blue);line-height:1.35}
.hero-panel p{font-size:5.6px;line-height:1.5;margin:6px 0 0 12px;position:relative;color:#444}
.hero-panel p::before{content:"›";position:absolute;left:-11px;top:-2px;font-size:8px;color:var(--blue)}
.hero-cta{display:flex;align-items:center;gap:12px;margin:10px 0 14px}
.btn-green{background:linear-gradient(#a9d64a,var(--green-dark));color:var(--white);font-size:6px;display:flex;align-items:center;justify-content:center;border-radius:2px}
.hero-cta .btn-green{width:105px;height:18px}
.hero-mail{font-size:6px;color:#333;display:flex;gap:3px;align-items:center}
.dots{left:360px;top:319px;display:flex;gap:4px}
.dots i{width:4px;height:4px;border-radius:50%;background:#999}
.dots i:first-child{background:var(--blue)}
/* countdown */
.section-title{width:734px;text-align:center;font-size:16px;font-weight:400;letter-spacing:.3px}
.countdown-title{top:367px;color:var(--blue)}
.count-box{top:410px;width:78px;height:80px;background:linear-gradient(#a3d242,var(--green-dark));color:var(--white);text-align:center;box-shadow:0 8px 6px -4px rgba(0,0,0,.35)}
.count-box b{display:block;font-size:30px;font-weight:400;line-height:1;margin-top:14px}
.count-box span{font-size:10px;display:block;margin-top:6px}
/* features */
.features{left:0;top:525px;width:734px;height:301px;background:linear-gradient(135deg,#3b7dc5,#2e6cb3)}
.feature{top:563px;width:176px}
.feature-photo{height:106px}
.feature h3{font-size:11px;font-weight:400;color:var(--white);margin:18px 0 9px}
.feature p{font-size:6.2px;line-height:11.7px;color:var(--white)}
.feature .btn-green{width:58px;height:16px;margin-top:11px;font-size:6px}
/* contact */
.contact-title{top:860px;color:var(--green)}
.social{top:900px;width:24px;height:24px;border-radius:50%;background:var(--blue)}
.contact-line{top:937px;width:734px;text-align:center;font-size:11px;color:#555}
/* footer */
.site-footer{left:0;top:996px;width:734px;height:204px;background:var(--green)}
.footer-head{top:1013px;font-size:7.5px;color:var(--white)}
.footer-links{top:1040px;list-style:none;font-size:6px;color:var(--white);line-height:14.6px}
.field{left:361px;width:141px;height:20px;background:#8cbc33;border:1px solid #a8d356;font-size:6px;color:var(--white);padding:6px 5px}
.message{left:505px;top:1038px;width:141px;height:71px;background:#8cbc33;border:1px solid #a8d356;font-size:6px;color:var(--white);padding:6px 7px}
.btn-send{left:361px;top:1116px;width:68px;height:19px;background:var(--blue);color:var(--white);font-size:6px;display:flex;align-items:center;justify-content:center}
.copyright{top:1176px;width:734px;text-align:center;font-size:7px;color:var(--white)}
</style>
</head>
<body>
<header class="abs site-header"></header>
<div class="abs top-info" style="left:88px">
  <svg width="7" height="7" viewBox="0 0 10 10"><path d="M2 0l2 2-1 2c1 1 2 2 3 3l2-1 2 2-2 2C4 10 0 6 0 2z" fill="#fff"/></svg>
  Phone Number (917) 555-0184
</div>
<div class="abs top-info" style="left:239px">
  <svg width="8" height="6" viewBox="0 0 10 7"><rect x=".5" y=".5" width="9" height="6" fill="none" stroke="#fff"/><path d="M.5 .5l4.5 3.5 4.5-3.5" fill="none" stroke="#fff"/></svg>
  Email info@levyreadynow.com
</div>
<div class="abs btn-appointment">SCHEDULE AN APPOINTMENT</div>
<div class="abs search">Search
  <svg width="7" height="7" viewBox="0 0 10 10"><circle cx="4" cy="4" r="3" fill="none" stroke="#9bcb3b" stroke-width="1.5"/><path d="M6.5 6.5L9 9" stroke="#9bcb3b" stroke-width="1.5"/></svg>
</div>
<div class="abs logo">LRN<small>levyreadynow.com</small></div>
<nav class="main-nav">
  <a class="active" style="left:274px">HOME</a>
  <a style="left:334px">ABOUT US</a>
  <a style="left:402px">SERVICES</a>
  <a style="left:473px">RESOURCES</a>
  <a style="left:586px">E-MAIL &amp; SOCIAL MEDIA ICONS</a>
</nav>
<div class="abs nav-marker"></div>

<div class="abs hero-photo" role="img" aria-label="Hand writing with a pen over tax forms and banknotes on a desk"></div>
<div class="abs hero-panel">
  <h2>The deadline for filing your 2015<br>Federal Tax Return is April 18, 2016</h2>
  <p>Don't wait! Set up an appointment to file your taxes now and receive the most money</p>
  <div class="hero-cta">
    <div class="btn-green">SCHEDULE APPOINTMENT</div>
    <div class="hero-mail">
      <svg width="7" height="5" viewBox="0 0 10 7"><rect x=".5" y=".5" width="9" height="6" fill="none" stroke="#333"/><path d="M.5 .5l4.5 3.5 4.5-3.5" fill="none" stroke="#333"/></svg>
      E-mail : mark@levyreadynow.com
    </div>
  </div>
  <h2>Why is Tax Day April 18?</h2>
  <p>The federal government is observing the Washington D.C. Emancipation holiday on April 15 so Tax Day is on the following Monday</p>
</div>
<div class="abs dots"><i></i><i></i><i></i></div>

<h2 class="abs section-title countdown-title">COUNTDOWN TO THE TAX DEADLINE</h2>
<div class="abs count-box" style="left:185px"><b>00</b><span>DAYS</span></div>
<div class="abs count-box" style="left:280px"><b>00</b><span>HOURS</span></div>
<div class="abs count-box" style="left:377px"><b>00</b><span>MINUTES</span></div>
<div class="abs count-box" style="left:470px"><b>00</b><span>SECONDS</span></div>

<section class="abs features" role="img" aria-label="Blue tinted background of printed financial documents"></section>
<div class="abs feature" style="left:87px">
  <div class="feature-photo" role="img" aria-label="Laptop and charts on a desk" style="background:linear-gradient(120deg,#eceef2,#c9cdd6 60%,#b9854f)"></div>
  <h3>SERVICES</h3>
  <p>At vero eos et accusamus et iusto odio dignissimos ducimus qui blanditiis praesentium voluptatum deleniti atque corrupti quos dolores et quas molestias excepturi sint occaecati cupiditate non provident, similique sunt in culpa qui officia deserunt mollitia animi ...Read More</p>
  <div class="btn-green">Services</div>
</div>
<div class="abs feature" style="left:279px">
  <div class="feature-photo" role="img" aria-label="Smiling man at a desk with a laptop" style="background:linear-gradient(#8ed3e6,#6fb6d4 60%,#e7e7e7)"></div>
  <h3>ABOUT US</h3>
  <p>At vero eos et accusamus et iusto odio dignissimos ducimus qui blanditiis praesentium voluptatum deleniti atque corrupti quos dolores et quas molestias excepturi sint occaecati cupiditate non provident, similique sunt in culpa qui officia deserunt mollitia animi ...Read More</p>
  <div class="btn-green">About Us</div>
</div>
<div class="abs feature" style="left:470px">
  <div class="feature-photo" role="img" aria-label="Woman reading a bill in a kitchen with a laptop" style="background:linear-gradient(120deg,#d9d4cc,#e8623c 55%,#c9c3ba)"></div>
  <h3>RESOURCES</h3>
  <p>At vero eos et accusamus et iusto odio dignissimos ducimus qui blanditiis praesentium voluptatum deleniti atque corrupti quos dolores et quas molestias excepturi sint occaecati cupiditate non provident, similique sunt in culpa qui officia deserunt mollitia animi ...Read More</p>
  <div class="btn-green">Resources</div>
</div>

<h2 class="abs section-title contact-title">CONTACT INFOMRATION</h2>
<svg class="abs" style="left:257px;top:904px" width="24" height="18" viewBox="0 0 24 18"><rect width="24" height="18" rx="2" fill="#0758a4"/><path d="M1 2l11 8 11-8" fill="none" stroke="#fff" stroke-width="2"/></svg>
<div class="abs social" style="left:306px"></div>
<div class="abs social" style="left:353px"></div>
<div class="abs social" style="left:401px"></div>
<div class="abs social" style="left:449px"></div>
<p class="abs contact-line">Phone: (917) 555-0184 &nbsp;|&nbsp; Email: info@levyreadynow.com</p>

<footer class="abs site-footer"></footer>
<div class="abs footer-head" style="left:88px">MENU LINKS</div>
<div class="abs footer-head" style="left:231px">OTHER LINKS</div>
<div class="abs footer-head" style="left:360px">CONTACT US</div>
<ul class="abs footer-links" style="left:87px">
  <li>HOME</li><li>ABOUT US</li><li>SERVICES</li><li>RESOURCES</li><li>E-MAIL &amp; SOCIAL MEDIA ICONS</li>
</ul>
<ul class="abs footer-links" style="left:232px">
  <li>TERMS AND CONDITIONS</li><li>PRIVAC POLICY</li><li>HELP</li>
</ul>
<div class="abs field" style="top:1038px">Subject</div>
<div class="abs field" style="top:1063px">E-Mail</div>
<div class="abs field" style="top:1088px">Phone Number</div>
<div class="abs message">Your Message</div>
<div class="abs btn-send">SEND MESSAGE</div>
<p class="abs copyright">© 2016 COMPANY NAME &nbsp;|&nbsp; ALL RIGHTS RESERVED</p>
</body>
</html>
```